Allied Health team of Physiotherapists & Occupational Therapists seek a business card design

We have our new logo, we now need our new business cards and stationary. Blossom: Lymphoedema & Women's Clinic is seeking a generic card design to represent our whole team and individual cards for each therapist that incorporates our new logo to communicate our holistic approach that is calming, nuturing, supportive and welcoming.
Our Physiotherapists and Occupational Therapists assess, treat and provide education for people who are at risk of or who have lymphoedema. This is often as a result of treatment for cancer. We provide pre-operative and post-operative management and cancer rehabilitation in our Pilates studio. Our team also consists of Physiotherapists who have a strong interest in pelvic floor and continence management for both men and women.

Target Market(s)

Mainly women health conscious

Industry/Entity Type

Allied Health: Physiotherapy / Occupational Therapy

Contact Information for Business Card

Address: 14 Calloway Ave Frankston 3199 Phone: 84317560 fax: 8431 7564 Email: info@blossomcarepartners.com.au Website: blossomcarepartners.com.au Facebook address: facebook.com/BlossomLymphoedemaAndWomensCareCentre. Room to write appointments. Individual cards need to have name, office email and individual email and professional details

Requirements
Must have
• Logo as per uploaded documents

```html
<!DOCTYPE html>
<html lang="en">
<head>
<meta charset="utf-8">
<title>Blossom Lymphoedema &amp; Women's Clinic – Business Cards</title>
<link rel="stylesheet" href="https://fonts.googleapis.com/css2?family=Marcellus&family=Open+Sans:wght@400;700&display=swap">
<style>
  :root {
    --backdrop: #1b1b1b;
    --card: #2f2f2f;
    --card-glow: #353534;
    --ink: #f2edd3;
  }
  * { box-sizing: border-box; margin: 0; padding: 0; }
  html, body {
    width: 1200px; height: 866px; overflow: hidden;
    background: var(--backdrop);
  }
  .sheet {
    width: 1200px; height: 866px;
    display: flex; flex-direction: column; align-items: center; justify-content: center;
    gap: 36px;
  }
  .card {
    position: relative;
    width: 620px; height: 379px;
    background: var(--card);
    color: var(--ink);
    overflow: hidden;
    box-shadow: 0 10px 24px rgba(0,0,0,0.45);
  }
  .ornament-area {
    position: absolute;
    left: 30px; top: 0;
    width: 500px; height: 240px;
    background: radial-gradient(ellipse at 50% 40%, var(--card-glow) 0%, var(--card) 70%);
  }
  .brand {
    position: absolute;
    right: 46px; top: 150px;
    display: flex; align-items: center; gap: 10px;
    font-family: "Marcellus", serif;
    font-size: 40px; line-height: 1;
    color: var(--ink);
  }
  .brand-dot {
    width: 16px; height: 16px; border-radius: 50%;
    border: 2px solid var(--ink);
  }
  .profile {
    position: absolute;
    left: 44px; top: 96px;
    font-family: "Open Sans", sans-serif;
    font-size: 12.5px; line-height: 1.45;
  }
  .profile-name {
    font-family: "Marcellus", serif;
    font-size: 27px; letter-spacing: 2px; font-weight: 400;
    margin-bottom: 8px;
  }
  .profile-role { font-weight: 700; }
  .contact {
    position: absolute;
    left: 44px; bottom: 80px;
    list-style: none;
    font-family: "Open Sans", sans-serif;
    font-size: 14px; line-height: 1.55;
  }
  .contact li { display: flex; align-items: center; gap: 9px; }
  .contact svg { width: 13px; height: 13px; flex: none; }
</style>
</head>
<body>
<main class="sheet">

  <section class="card card-front">
    <div class="ornament-area" role="img" aria-label="Faint decorative leafy branch ornament"></div>
    <div class="profile">
      <h1 class="profile-name">MARISA DALTON</h1>
      <p>B. Physio (Hons), B.App.Sci.(Human Movement/Psych)</p>
      <p>Post Grad Certif. Exercise for Women</p>
      <p>Post Grad Certif. Continence &amp; Pelvic Floor Rehabilitation</p>
      <p class="profile-role">Physiotherapist</p>
      <p class="profile-role">Lymphoedema &amp; Oncology Rehabilitation</p>
      <p class="profile-role">Continence &amp; Pelvic Floor</p>
    </div>
    <div class="brand"><span class="brand-dot"></span>Blossom</div>
  </section>

  <section class="card card-back">
    <div class="ornament-area" role="img" aria-label="Faint decorative leafy branch ornament"></div>
    <ul class="contact">
      <li>
        <svg viewBox="0 0 16 16" aria-hidden="true"><path fill="var(--ink)" d="M3.5 1.5l2.5 3-1.5 1.5c.8 2 2.5 3.7 4.5 4.5L10.5 9l3 2.5-1.5 2.5C7 14 2 9 2 3z"/></svg>
        000 3456 7890
      </li>
      <li>
        <svg viewBox="0 0 16 16" aria-hidden="true"><rect x="1" y="3" width="14" height="10" fill="var(--ink)"/><path d="M1 3l7 6 7-6" fill="none" stroke="var(--card)" stroke-width="1.4"/></svg>
        info@blossomcarepartners.com.au
      </li>
      <li>
        <svg viewBox="0 0 16 16" aria-hidden="true"><rect x="1" y="3" width="14" height="10" fill="var(--ink)"/><path d="M1 3l7 6 7-6" fill="none" stroke="var(--card)" stroke-width="1.4"/></svg>
        name@blossomcarepartners.com.au
      </li>
      <li>
        <svg viewBox="0 0 16 16" aria-hidden="true"><circle cx="8" cy="8" r="6.5" fill="var(--ink)"/><path d="M1.5 8h13M8 1.5v13M3 4.5h10M3 11.5h10" stroke="var(--card)" stroke-width="1" fill="none"/><ellipse cx="8" cy="8" rx="3" ry="6.5" fill="none" stroke="var(--card)" stroke-width="1"/></svg>
        www.blossomcarepartners.com.au
      </li>
    </ul>
    <div class="brand"><span class="brand-dot"></span>Blossom</div>
  </section>

</main>
</body>
</html>
```